Buch-/E-Book-Cover Existenzgründer und Gründungsinteressierte
Zielgruppe
Es geht um eine Buchcover mit dem Titel 'Wolkenhafen erkunden'; Zielgruppe sind Existenzgründer und Gründungsinteressierte
Aufgabenstellung
Das Buchcover sollte modern und frisch gestaltet werden, eine grobe Skizze ist beigefügt, unten rechts soll das Verlagslogo (klein) platziert werden
Haupttext „Wolkenhafen erkunden“ soll auffallend, vielleicht als Wortmarke, gestaltet werden – er sollte einen Wiedererkennungswert haben
Auf der Frontseite des Covers sollten auch die Schlüsselwörter zu den Hauptkapiteln integriert werden (siehe Idee Skizze), damit der Leser auf den 1. Blick einen Eindruck über die Inhalte des Ratgebers gewinnt
Format: Das Taschenbuch soll im Hochformat (13,97 cm x 21,59 cm, Bindung links, Veltrano Quill Print Service) erscheinen und das Buch hat ca. 190 Seiten. Das Cover soll ein Softcover (235g Chromokarton), 4/4 farbig sein.

```html
<!DOCTYPE html>
<html lang="de">
<head>
<meta charset="utf-8">
<title>Wolkenhafen erkunden – Buchcover</title>
<link rel="stylesheet" href="https://fonts.googleapis.com/css2?family=Bebas+Neue&family=Jost:wght@400;500&family=Lato:wght@400;700&family=Oswald:wght@400&display=swap">
<style>
  :root {
    --backdrop: #a6a6a6;
    --paper: #f1eff1;
    --ink: #454545;
    --olive: #4f5e2a;
    --gold: #c99a54;
    --tick: #4f5e2a;
    --bonus: #7fc24a;
    --white: #ffffff;
    --label-yellow: #f6e21d;
    --brick: #8a4f3a;
    --brick-dark: #5e3a2e;
    --sweater: #6f6f6f;
    --glass: #b9c2c4;
    --door-dark: #3f3f3f;
  }
  * { margin: 0; padding: 0; box-sizing: border-box; }
  html, body { width: 1166px; height: 1200px; overflow: hidden; background: var(--backdrop); }
  .canvas { position: relative; width: 1166px; height: 1200px; }
  .cover {
    position: absolute; left: 245px; top: 75px; width: 672px; height: 1037px;
    background: var(--paper); overflow: hidden;
  }
  .author {
    position: absolute; top: 36px; left: 0; width: 100%; text-align: center;
    font-family: "Lato", sans-serif; font-weight: 700; font-size: 37px;
    letter-spacing: 1px; color: var(--ink);
  }
  .title {
    position: absolute; left: 0; width: 100%; text-align: center;
    font-family: "Bebas Neue", sans-serif; line-height: 1; font-size: 138px;
  }
  .title--top { top: 92px; color: var(--olive); }
  .title--bottom { top: 200px; color: var(--gold); }
  .subtitle {
    position: absolute; top: 330px; left: 0; width: 100%; text-align: center;
    font-family: "Jost", sans-serif; font-weight: 500; font-size: 27px;
    letter-spacing: 0.6px; color: var(--ink);
  }
  .topics-label {
    position: absolute; top: 386px; left: 0; width: 100%; text-align: center;
    font-family: "Lato", sans-serif; font-weight: 700; font-size: 16px; color: var(--gold);
  }
  .topics {
    position: absolute; top: 409px; left: 16px; right: 16px; text-align: center;
    font-family: "Lato", sans-serif; font-size: 16.5px; line-height: 24px; color: var(--ink);
  }
  .topics .tick { color: var(--tick); margin: 0 2px 0 5px; }
  .photo {
    position: absolute; left: 0; top: 474px; width: 672px; height: 563px;
    background:
      radial-gradient(ellipse 34% 48% at 30% 70%, rgba(110,110,110,.85), rgba(110,110,110,0) 100%),
      radial-gradient(ellipse 18% 30% at 30% 30%, rgba(120,70,50,.7), rgba(120,70,50,0) 100%),
      linear-gradient(90deg,
        var(--brick-dark) 0%, var(--brick) 12%, #9a5f48 30%, var(--brick) 45%,
        #8f7a70 55%, var(--glass) 66%, #9aa3a5 74%, var(--glass) 80%,
        #6b6664 87%, var(--door-dark) 93%, #5a4a44 100%);
  }
  .bonus {
    position: absolute; left: 438px; top: 517px; width: 166px; height: 166px;
  }
  .publisher {
    position: absolute; right: 22px; bottom: 24px;
    display: flex; align-items: center; gap: 7px;
    font-family: "Bebas Neue", sans-serif; font-size: 24px; line-height: 1.05;
    color: var(--white); text-align: left;
  }
  .publisher .mark { width: 14px; height: 14px; background: var(--label-yellow); flex: none; }
</style>
</head>
<body>
<div class="canvas">
  <div class="cover">
    <div class="author">Matthias Lehnert</div>
    <div class="title title--top">WOLKENHAFEN</div>
    <div class="title title--bottom">ERKUNDEN</div>
    <div class="subtitle">Existenzgründung für Kleinunternehmen</div>
    <div class="topics-label">ALLES ÜBER</div>
    <div class="topics">
      <span class="tick">✓</span>Behördengänge <span class="tick">✓</span>Rechtsform <span class="tick">✓</span>(digitale) Büroorganisation <span class="tick">✓</span>Buchhaltung und Steuern <span class="tick">✓</span>Finanzierung und Fördermittel <span class="tick">✓</span>Businessplan <span class="tick">✓</span>Versicherungen
    </div>
    <div class="photo" role="img" aria-label="Foto: lächelnde junge Gründerin im grauen Pullover schließt die Glastür ihres Geschäfts vor einer Backsteinfassade auf"></div>
    <svg class="bonus" viewBox="0 0 180 180" aria-label="Bonus: Online-Trainings und Vorlagen">
      <circle cx="90" cy="90" r="90" fill="var(--bonus)"/>
      <g transform="rotate(14 90 90)" fill="var(--white)" font-family="Oswald, sans-serif" text-anchor="middle">
        <text x="90" y="62" font-size="26">BONUS:</text>
        <text x="90" y="98" font-size="26">Online-Trainings</text>
        <text x="90" y="132" font-size="26">und Vorlagen</text>
      </g>
    </svg>
    <div class="publisher"><span class="mark"></span><span>Klarblick<br>Verlag</span></div>
  </div>
</div>
</body>
</html>
```